Personal training and nutrition business needs business card design

We need a business card that outlays our services and invites potential customers to join our team and take the first step to a healthier and more enjoyable life. We cater for any level of fitness and specialize in weight loss and conditioning, strength training, muscle gain and strength endurance. Whether you are just starting off or need some help getting to the next level of your journey we are here to get the job done.
We specialize in one on one or one on two personal training sessions and each program will be custom made to suit individual fitness goals of our clients

```html
<!DOCTYPE html>
<html lang="en">
<head>
<meta charset="utf-8">
<title>Stride &amp; Tempo — Business Card</title>
<link href="https://fonts.googleapis.com/css2?family=Roboto:wght@400;500;900&family=Saira+Condensed:wght@500&display=swap" rel="stylesheet">
<style>
  :root {
    --backdrop: #2a2a2a;
    --purple-deep: #573a86;
    --purple-mid: #7a4a98;
    --purple-light: #9d56a0;
    --paper: #f2f1f2;
    --ink: #1b1b1b;
    --text: #333333;
    --white: #ffffff;
    --tag-light: #e4dcec;
    --brand-gradient: linear-gradient(120deg, var(--purple-deep) 0%, var(--purple-mid) 55%, var(--purple-light) 100%);
  }
  * { margin: 0; padding: 0; box-sizing: border-box; }
  html, body { width: 1200px; height: 1138px; overflow: hidden; }
  body {
    background: var(--backdrop);
    position: relative;
    font-family: "Roboto", Arial, sans-serif;
  }
  .card {
    position: absolute;
    width: 620px;
    height: 376px;
    border-radius: 16px;
    overflow: hidden;
  }
  /* Front */
  .card-front {
    left: 274px; top: 186px;
    background: var(--brand-gradient);
  }
  .front-brand {
    position: absolute;
    left: 0; right: 0; top: 152px;
    text-align: center;
    color: var(--white);
    font-weight: 900;
    font-size: 44px;
    letter-spacing: 1px;
    text-transform: uppercase;
  }
  .front-tagline {
    position: absolute;
    left: 0; right: 0; top: 210px;
    text-align: center;
    color: var(--tag-light);
    font-weight: 500;
    font-size: 16px;
    letter-spacing: 2px;
    text-transform: uppercase;
  }
  /* Back */
  .card-back {
    left: 276px; top: 607px;
    background: var(--paper);
  }
  .monogram-area {
    position: absolute;
    left: 0; top: 17px;
    width: 372px; height: 340px;
  }
  .monogram-upper,
  .monogram-lower {
    position: absolute;
    left: 0;
    background: var(--brand-gradient);
    background-size: 372px 340px;
  }
  .monogram-upper {
    top: 0;
    width: 372px; height: 200px;
    border-radius: 0 36px 36px 0;
  }
  .monogram-lower {
    top: 150px;
    width: 262px; height: 190px;
    border-radius: 0 0 36px 0;
    background-position: 0 -150px;
  }
  .edge-tab {
    position: absolute;
    right: -14px; top: 160px;
    width: 28px; height: 50px;
    border-radius: 50%;
    background: var(--purple-mid);
  }
  .back-brand {
    position: absolute;
    left: 402px; top: 30px;
    color: var(--ink);
    font-weight: 900;
    font-size: 29px;
    line-height: 32px;
    text-transform: uppercase;
  }
  .back-tagline {
    position: absolute;
    left: 402px; top: 102px;
    color: var(--purple-mid);
    font-weight: 500;
    font-size: 7.5px;
    letter-spacing: 0.3px;
    text-transform: uppercase;
  }
  .person {
    position: absolute;
    right: 38px; top: 156px;
    text-align: right;
  }
  .person-name {
    font-family: "Saira Condensed", "Arial Narrow", sans-serif;
    font-weight: 500;
    font-size: 26px;
    line-height: 30px;
    color: var(--purple-mid);
  }
  .person-role {
    font-size: 16px;
    color: var(--text);
    margin-top: 2px;
  }
  .contact-list {
    position: absolute;
    right: 38px; top: 238px;
    list-style: none;
  }
  .contact-list li {
    display: flex;
    justify-content: flex-end;
    align-items: center;
    height: 24px;
    font-size: 15px;
    color: var(--text);
  }
  .contact-list svg { margin-left: 10px; width: 14px; height: 14px; fill: var(--purple-mid); }
  .contact-list .accent { color: var(--purple-mid); }
  .address {
    position: absolute;
    right: 38px; top: 318px;
    font-size: 15px;
    color: var(--text);
  }
</style>
</head>
<body>
  <section class="card card-front">
    <div class="front-brand">Stride &amp; Tempo</div>
    <div class="front-tagline">Personal Training &nbsp;|&nbsp; Nutrition &nbsp;|&nbsp; Motivation</div>
  </section>

  <section class="card card-back">
    <div class="monogram-area" role="img" aria-label="Large brand monogram decoration in purple gradient">
      <div class="monogram-upper"></div>
      <div class="monogram-lower"></div>
    </div>
    <div class="edge-tab"></div>
    <div class="back-brand">Stride<br>&amp; Tempo</div>
    <div class="back-tagline">Personal Training. Nutrition. Motivation</div>
    <div class="person">
      <div class="person-name">Marcus Reed</div>
      <div class="person-role">Personal Trainer</div>
    </div>
    <ul class="contact-list">
      <li>+1 (555) 214-3380
        <svg viewBox="0 0 16 16" aria-hidden="true"><path d="M2 6c0-2 3-4 6-4s6 2 6 4v1h-3V5.5c-1-.6-5-.6-6 0V7H2z M4 8h8l2 6H2z"/></svg>
      </li>
      <li>marcus@strideandtempo.com
        <svg viewBox="0 0 16 16" aria-hidden="true"><path d="M1 3h14v10H1z M2 4l6 5 6-5" fill="none" stroke="#7a4a98" stroke-width="1.6"/></svg>
      </li>
      <li>www.<span class="accent">strideandtempo</span>.com
        <svg viewBox="0 0 16 16" aria-hidden="true"><g fill="none" stroke="#7a4a98" stroke-width="1.3"><circle cx="8" cy="8" r="6.3"/><ellipse cx="8" cy="8" rx="2.8" ry="6.3"/><path d="M1.7 8h12.6M2.8 4.6h10.4M2.8 11.4h10.4"/></g></svg>
      </li>
    </ul>
    <div class="address">1428 Cedar Ridge Lane Austin Texas 78704</div>
  </section>
</body>
</html>
```